Business Card Design

I need a business card design for a photography business that specializes in headshots and portraits.

Target Market(s)

Business professionals, actors, actresses

Industry/Entity Type

Business

Contact Information for Business Card

Corvin Lane Photography, Greg Wilmot, 1187 Kestrel Avenue, Suite 416, Fort Wayne, IN 46815, 260.555.0148, www.corvinlanephoto.example. greg.wilmot@corvinlanephoto.example

Requirements
Must have
• The business card should state the type of photography services offered: headshots and portraits.

```html
<!DOCTYPE html>
<html lang="en">
<head>
<meta charset="utf-8">
<title>Corvin Lane Photography – Business Card</title>
<link rel="stylesheet" href="https://fonts.googleapis.com/css2?family=Jost:wght@400;500;600&display=swap">
<style>
  :root {
    --page-bg: #9a9a9a;
    --card-white: #ffffff;
    --ink-dark: #3a3d44;
    --ink-grey: #3f4248;
    --brand-pink: #c4538d;
    --rose: #e06a93;
    --orange: #ef9a45;
    --yellow: #fef574;
    --band-grey: #bdbdbd;
    --photo-light: #e4e4e4;
    --photo-mid: #a9a9a9;
  }
  * { margin: 0; padding: 0; box-sizing: border-box; }
  html, body { width: 1200px; height: 1200px; overflow: hidden; }
  body { background: var(--page-bg); position: relative; font-family: "Jost", sans-serif; }

  .card {
    position: absolute; left: 100px; top: 323px;
    width: 1000px; height: 553px;
    background: var(--card-white); overflow: hidden;
  }
  .card-bands { position: absolute; inset: 0; width: 1000px; height: 553px; }

  .brand-name {
    position: absolute; left: 47px; top: 124px;
    font-size: 44px; font-weight: 400; color: var(--brand-pink);
    line-height: 1; white-space: nowrap;
  }
  .studio-address {
    position: absolute; left: 47px; top: 176px;
    font-size: 22px; line-height: 31px; color: var(--ink-grey); font-weight: 400;
    white-space: nowrap;
  }
  .services {
    position: absolute; left: 47px; top: 254px;
    font-size: 18px; line-height: 1; font-weight: 500; letter-spacing: 2px;
    text-transform: uppercase; color: var(--brand-pink); white-space: nowrap;
  }
  .portrait-art {
    position: absolute; left: 600px; top: 53px; width: 362px; height: 236px;
    background: linear-gradient(135deg, var(--photo-light), var(--photo-mid));
    border-radius: 4px;
  }
  .person-name {
    position: absolute; left: 64px; top: 428px;
    font-size: 46px; font-weight: 600; color: var(--card-white); line-height: 1;
    white-space: nowrap;
  }
  .online-contact {
    position: absolute; right: 98px; top: 352px;
    text-align: right; font-size: 21px; line-height: 30px; color: var(--ink-grey);
    white-space: nowrap;
  }
  .phone-number {
    position: absolute; right: 98px; top: 446px;
    font-size: 44px; line-height: 1; color: var(--ink-grey); letter-spacing: 1px;
    white-space: nowrap;
  }
  .icon { position: absolute; }
  .icon-monitor { left: 918px; top: 356px; width: 56px; height: 52px; }
  .icon-phone { left: 916px; top: 448px; width: 58px; height: 46px; }
</style>
</head>
<body>
  <div class="card">
    <svg class="card-bands" viewBox="0 0 1000 553" aria-hidden="true">
      <polygon fill="var(--ink-dark)" points="0,343 409,343 538,553 0,553"/>
      <polygon fill="var(--band-grey)" points="418,343 1000,343 1000,423 467,423"/>
      <polygon fill="var(--band-grey)" points="472,431 1000,431 1000,512 522,512"/>
      <polygon fill="var(--brand-pink)" points="527,512 640,512 665,553 552,553"/>
      <polygon fill="var(--rose)" points="640,512 758,512 783,553 665,553"/>
      <polygon fill="var(--orange)" points="758,512 891,512 916,553 783,553"/>
      <polygon fill="var(--yellow)" points="891,512 1000,512 1000,553 916,553"/>
    </svg>

    <div class="brand-name">Corvin Lane Photography</div>
    <div class="studio-address">1187 Kestrel Avenue, Suite 416,<br>Fort Wayne, IN 46815</div>
    <div class="services">Headshots &amp; Portraits</div>

    <div class="portrait-art" role="img" aria-label="Stack of three tilted portrait prints showing headshot silhouettes"></div>

    <div class="person-name">Greg Wilmot</div>

    <div class="online-contact">www.corvinlanephoto.example<br>greg.wilmot@corvinlanephoto.example</div>
    <svg class="icon icon-monitor" viewBox="0 0 56 52" aria-hidden="true">
      <rect x="2" y="2" width="52" height="36" rx="3" fill="var(--ink-dark)"/>
      <rect x="7" y="7" width="42" height="26" fill="var(--band-grey)"/>
      <rect x="23" y="38" width="10" height="8" fill="var(--ink-dark)"/>
      <rect x="14" y="46" width="28" height="4" rx="1" fill="var(--ink-dark)"/>
    </svg>

    <div class="phone-number">260.555.0148</div>
    <svg class="icon icon-phone" viewBox="0 0 58 46" aria-hidden="true">
      <path d="M3 14 C3 4 55 4 55 14 L55 19 L44 19 L44 13 C36 10 22 10 14 13 L14 19 L3 19 Z" fill="var(--ink-dark)"/>
      <path d="M18 16 L40 16 L50 42 L8 42 Z" fill="var(--ink-dark)"/>
      <g fill="var(--band-grey)">
        <rect x="20" y="24" width="4" height="3"/><rect x="27" y="24" width="4" height="3"/><rect x="34" y="24" width="4" height="3"/>
        <rect x="18" y="30" width="4" height="3"/><rect x="27" y="30" width="4" height="3"/><rect x="36" y="30" width="4" height="3"/>
        <rect x="16" y="36" width="4" height="3"/><rect x="27" y="36" width="4" height="3"/><rect x="38" y="36" width="4" height="3"/>
      </g>
    </svg>
  </div>
</body>
</html>
```